Square graphic for social media post

I want to create a 1080 x 1080px all-black image for the quote below that I can share on social media. I want the emphasis to be primarily on the quote, secondarily on the portrait, and third (smallest) on the logo. I want the background on the portrait to be edited so it's transparent and just shows the face of the person on a black background (no brick wall visible).

Graphic color: black
Text color: white
Content: "What we went through is going to make the greatest generation of hoteliers our industry has ever seen." << biggest text
Dorian Welk << smaller text
President, Marrowgate Hotels << smaller text
[image of person - use whichever version looks better to you]
[Add Lodging Ledger logo - whichever looks better to you]

This image needs to be readable when sized down much smaller (400x400?) so want the text and portrait to take up most of the space.

I'd like the output both as PNG and original file (preferably Canva). Thanks!

Target Market(s)

Hotel managers

Industry/Entity Type

Hospitality

Font styles to use
Sans Serif

Colors

Designer to choose colors to be used in the design.

Requirements
Must have
• Needs to focus on the quote and the person quoted (the portrait)

```html
<!DOCTYPE html>
<html lang="en">
<head>
<meta charset="utf-8">
<title>Dorian Welk Quote</title>
<link href="https://fonts.googleapis.com/css2?family=Inter:ital,wght@0,400;0,500;0,600;1,400&display=swap" rel="stylesheet">
<style>
  :root {
    --bg: #060709;
    --ink: #ffffff;
    --ink-soft: #e9eaec;
    --portrait-top: #0c0d0f;
    --portrait-mid: #9c7a6c;
    --portrait-suit: #1f3a78;
  }
  html, body {
    margin: 0;
    padding: 0;
    width: 1200px;
    height: 1200px;
    overflow: hidden;
    background: var(--bg);
  }
  .post {
    position: relative;
    width: 1200px;
    height: 1200px;
    background: var(--bg);
    font-family: "Inter", sans-serif;
    color: var(--ink);
  }
  .quote-mark {
    position: absolute;
    left: 571px;
    top: 127px;
    width: 59px;
    height: 38px;
  }
  .quote-text {
    position: absolute;
    left: 130px;
    top: 182px;
    width: 1010px;
    margin: 0;
    font-style: italic;
    font-weight: 400;
    font-size: 56px;
    line-height: 105px;
    letter-spacing: 0.5px;
    white-space: nowrap;
  }
  .quote-line {
    display: block;
  }
  .portrait {
    position: absolute;
    left: 379px;
    top: 516px;
    width: 428px;
    height: 428px;
    border-radius: 50%;
    background:
      radial-gradient(ellipse 34% 40% at 50% 42%, var(--portrait-mid) 0%, #7a5d52 55%, transparent 80%),
      linear-gradient(to bottom, var(--portrait-top) 0%, var(--portrait-top) 65%, var(--portrait-suit) 100%);
  }
  .brand {
    position: absolute;
    left: 862px;
    top: 706px;
    width: 200px;
    text-align: center;
    font-weight: 600;
    font-size: 17px;
    letter-spacing: 3px;
    text-transform: uppercase;
    color: var(--ink);
  }
  .brand-dot {
    display: block;
    width: 10px;
    height: 10px;
    margin: 0 auto 10px;
    border-radius: 50%;
    background: var(--ink);
  }
  .speaker {
    position: absolute;
    left: 0;
    top: 992px;
    width: 1176px;
    text-align: center;
  }
  .speaker-name {
    margin: 0;
    font-weight: 500;
    font-size: 38px;
    letter-spacing: 5px;
    text-transform: uppercase;
  }
  .speaker-role {
    margin: 10px 0 0;
    font-weight: 400;
    font-size: 22px;
    letter-spacing: 5px;
    text-transform: uppercase;
    color: var(--ink-soft);
  }
</style>
</head>
<body>
  <main class="post">
    <svg class="quote-mark" viewBox="0 0 59 38" aria-hidden="true">
      <path fill="#ffffff" d="M12 0a12 12 0 0 1 12 12c0 10-6 19-14 26l-1-2c4-4 6-8 6-12A12 12 0 0 1 12 0z"/>
      <path fill="#ffffff" d="M46 0a12 12 0 0 1 12 12c0 10-6 19-14 26l-1-2c4-4 6-8 6-12A12 12 0 0 1 46 0z"/>
    </svg>

    <p class="quote-text">
      <span class="quote-line">What we went through is going to</span>
      <span class="quote-line">make the greatest generation of</span>
      <span class="quote-line">hoteliers our industry has ever seen.</span>
    </p>

    <div class="portrait" role="img" aria-label="Portrait of Dorian Welk on a black background"></div>

    <div class="brand">
      <span class="brand-dot"></span>
      Lodging Ledger
    </div>

    <div class="speaker">
      <p class="speaker-name">Dorian Welk</p>
      <p class="speaker-role">President, Marrowgate Hotels</p>
    </div>
  </main>
</body>
</html>
```